Premium Gold Vodka Label Design

English ------------------- We need a label for a Vodka Bottle. Its a sparkling premium vodka with gold inside. The design should look premium. We tried it on our selves but it looks horrible. Therefore we need your help. The current name is glimora K, but we are open for any better suggestion. We attached the selfmade design. The label will be printed on the bottle. We have other design jobs for you (logo, other sorts)! English ------------------------ We need a label for a vodka bottle. This is a premium vodka which is offset with gold. The design should look like this. We have tried so far and failed. That is why we need your support. The name is so far glimora K. If you have better suggestions we would be pleased about other suggestions / ideas. In the appendix the failed design is stored. The label is to be applied by screen printing. In the case of good work follow-up projects are guaranteed (logo, other varieties, etc)!

Target Market(s)

USA

Colors

Designer to choose colors to be used in the design.

Requirements
Must have
• English ------------------------ The needed text is on our selfmade label that is attached. English ------------------------ The required texts are stored in the attached design.
Nice to have
• English ------------------------ Transparent places are allowed because we want to print the label on the bottom. English ------------------------ As the label is applied by screen printing, transparent areas are also possible.

```html
<!DOCTYPE html>
<html lang="en">
<head>
<meta charset="utf-8">
<title>Glimora K Premium Gold Sparkling Vodka Label</title>
<link rel="stylesheet" href="https://fonts.googleapis.com/css2?family=Playfair+Display:wght@700;900&family=Great+Vibes&display=swap">
<style>
  :root {
    --bg: #ecebe6;
    --gold-light: #ffe27a;
    --gold: #f2b718;
    --gold-deep: #b9800a;
    --ink: #141210;
    --red: #c8251c;
    --red-deep: #8e1410;
    --maroon: #6e0f0c;
    --cream: #fbe6b0;
  }
  * { margin: 0; padding: 0; box-sizing: border-box; }
  html, body { width: 885px; height: 1200px; overflow: hidden; }
  body {
    background: var(--bg);
    font-family: "Playfair Display", Georgia, serif;
    position: relative;
  }
  .neck-label {
    position: absolute; left: 302px; top: 80px;
    width: 280px; height: 190px;
  }
  .neck-label svg, .main-label svg { position: absolute; inset: 0; }
  .neck-script {
    position: absolute; top: 30px; width: 100%; text-align: center;
    font-family: "Great Vibes", cursive; font-size: 20px; color: var(--gold-light);
  }
  .neck-brand {
    position: absolute; top: 84px; width: 100%; text-align: center;
    font-size: 24px; font-weight: 700; letter-spacing: 3px; color: var(--cream);
  }
  .neck-year {
    position: absolute; top: 128px; width: 100%; text-align: center;
    font-size: 24px; font-weight: 700; color: var(--gold-light);
  }
  .main-label {
    position: absolute; left: 222px; top: 320px;
    width: 440px; height: 800px;
  }
  .label-title {
    position: absolute; top: 108px; width: 100%; text-align: center;
    font-size: 50px; font-weight: 900; color: var(--ink); letter-spacing: 1px;
  }
  .label-subtitle {
    position: absolute; top: 196px; width: 100%; text-align: center;
    font-size: 13px; font-weight: 700; color: var(--ink); letter-spacing: 0.5px;
  }
  .brand-name {
    position: absolute; top: 345px; width: 100%; text-align: center;
    font-size: 34px; font-weight: 700; letter-spacing: 4px; color: var(--gold-light);
  }
  .label-details {
    position: absolute; left: 80px; top: 505px;
    font-size: 16px; font-weight: 700; color: var(--ink); line-height: 1.6;
  }
  .label-details .amp { color: var(--red); font-size: 22px; }
  .label-strength {
    position: absolute; left: 80px; right: 80px; top: 618px;
    display: flex; justify-content: space-between;
    font-size: 12px; font-weight: 700; color: var(--ink);
  }
  .label-volume {
    position: absolute; top: 665px; width: 100%; text-align: center;
    font-size: 20px; font-weight: 700; color: var(--ink);
  }
</style>
</head>
<body>

<div class="neck-label">
  <svg viewBox="0 0 280 190" width="280" height="190">
    <defs>
      <linearGradient id="neckGold" x1="0" y1="0" x2="1" y2="1">
        <stop offset="0" stop-color="var(--gold-light)"/>
        <stop offset="0.5" stop-color="var(--gold)"/>
        <stop offset="1" stop-color="var(--gold-deep)"/>
      </linearGradient>
    </defs>
    <path d="M40,12 L240,12 L262,50 L262,145 L240,180 L40,180 L18,145 L18,50 Z" fill="url(#neckGold)"/>
    <path d="M46,20 L234,20 L254,54 L254,141 L234,172 L46,172 L26,141 L26,54 Z" fill="var(--maroon)"/>
    <rect x="0" y="72" width="280" height="52" fill="var(--red)"/>
    <rect x="0" y="72" width="280" height="3" fill="var(--gold)"/>
    <rect x="0" y="121" width="280" height="3" fill="var(--gold)"/>
    <path d="M0,124 L14,136 L14,124 Z M280,124 L266,136 L266,124 Z" fill="var(--red-deep)"/>
  </svg>
  <div class="neck-script">Premium Gold</div>
  <div class="neck-brand">GLIMORA K</div>
  <div class="neck-year">1974</div>
</div>

<div class="main-label">
  <svg viewBox="0 0 440 800" width="440" height="800">
    <defs>
      <linearGradient id="labelGold" x1="0" y1="0" x2="1" y2="0">
        <stop offset="0" stop-color="var(--gold-deep)"/>
        <stop offset="0.3" stop-color="var(--gold)"/>
        <stop offset="0.55" stop-color="var(--gold-light)"/>
        <stop offset="0.8" stop-color="var(--gold)"/>
        <stop offset="1" stop-color="var(--gold-deep)"/>
      </linearGradient>
      <path id="labelShape" d="M0,90 Q40,90 40,50 L40,40 Q120,40 150,0 L290,0 Q320,40 400,40 L400,50 Q400,90 440,90 L440,710 Q400,710 400,750 L400,760 Q320,760 290,800 L150,800 Q120,760 40,760 L40,750 Q40,710 0,710 Z"/>
    </defs>
    <use href="#labelShape" fill="url(#labelGold)"/>
    <use href="#labelShape" fill="var(--ink)" transform="translate(14 17) scale(0.936 0.958)"/>
    <use href="#labelShape" fill="url(#labelGold)" transform="translate(28 34) scale(0.873 0.915)"/>
    <rect x="0" y="270" width="440" height="200" fill="var(--red)"/>
    <rect x="0" y="270" width="440" height="4" fill="var(--red-deep)"/>
    <rect x="0" y="466" width="440" height="4" fill="var(--red-deep)"/>
  </svg>
  <div class="label-title">VODKA</div>
  <div class="label-subtitle">PREMIUM GOLD SPARKLING</div>
  <div class="brand-name">GLIMORA K</div>
  <div class="label-details">
    Distilled <span class="amp">&amp;</span> Filtered<br>
    Made in Germany
  </div>
  <div class="label-strength"><span>40% Alc Vol</span><span>80Proof</span></div>
  <div class="label-volume">200ml</div>
</div>

</body>
</html>
```